Occupational Therapist does home accessibility for disabled folks; needs business card design

We need a business card for a company in Portland, Oregon that specializes in making homes accessible, comfortable, and functional for people who are disabled or aging who would like to stay in THEIR home. Our medical background as Occupational Therapists allows us to translate the functional needs of the person into the recommendations for the design of the home remodel.

Target Market(s)

Elderly, children of elderly
People with disabilities, families of people with disabilities

Industry/Entity Type

Business

Contact Information for Business Card

Company name: HomeWise
Name: Danielle Reyes Crawford, OTR/L, CAPS, ECHM
Occupational Therapist, Home Modification & Accessibility Specialist
website: www.homewiseforyears.com
email: homewiseforyears@nestmail.example
phone: (503)218-4057
CCB #: 487315

Font styles to use
Sans Serif

Requirements
Must have
• My logo
• Easy to read font with contrasting background
• Please list the Services offered: Occupational Therapy, Home safety & accessibility assessments, Home modification consulting, project management
Nice to have
• Friendly, welcoming feel
Should not have
• Dark colored background

```html
<!DOCTYPE html>
<html lang="en">
<head>
<meta charset="utf-8">
<title>HomeWise Business Card</title>
<link rel="stylesheet" href="https://fonts.googleapis.com/css2?family=Nunito:wght@400;600;700;800&display=swap">
<style>
  :root {
    --canvas-bg: #ece8e3;
    --card-white: #ffffff;
    --rust-dark: #8e2a12;
    --rust-mid: #c2501a;
    --amber: #ee7d1b;
    --ink: #1d1d1d;
    --slate: #4b4b4d;
    --label-bg: #555557;
  }
  * { box-sizing: border-box; margin: 0; padding: 0; }
  html, body {
    width: 1200px; height: 1000px; overflow: hidden;
    background: var(--canvas-bg);
    font-family: "Nunito", sans-serif;
  }
  .canvas { position: relative; width: 1200px; height: 1000px; }

  .card {
    position: absolute; left: 228px; width: 745px; height: 424px;
    background: var(--card-white);
    box-shadow: 0 6px 18px rgba(0,0,0,0.18);
    overflow: hidden;
  }
  .card--front { top: 22px; }
  .card--back { top: 510px; }

  .warm-band {
    position: absolute;
    background:
      radial-gradient(ellipse at 55% 55%, var(--amber) 0%, var(--rust-mid) 45%, var(--rust-dark) 100%);
  }
  .warm-band--top-left { left: 0; top: 26px; width: 70px; height: 104px; }
  .warm-band--top-right { left: 272px; top: 26px; width: 473px; height: 104px; }
  .warm-band--bottom { left: 0; top: 386px; width: 745px; height: 38px; }

  .brand {
    position: absolute; left: 74px; top: 26px; width: 194px; height: 104px;
    display: flex; align-items: center; justify-content: center; gap: 8px;
  }
  .brand__mark { flex: none; width: 14px; height: 14px; background: var(--rust-mid); }
  .brand__name { font-size: 30px; font-weight: 700; color: var(--slate); letter-spacing: -0.5px; white-space: nowrap; }

  .person { position: absolute; left: 14px; top: 174px; width: 262px; }
  .person__name { font-size: 22px; font-weight: 800; color: var(--ink); white-space: nowrap; letter-spacing: -0.3px; }
  .person__creds { font-size: 11px; font-weight: 800; color: var(--ink); text-align: right; margin-top: 1px; }
  .person__role { font-size: 18px; line-height: 25px; color: var(--slate); margin-top: 24px; white-space: nowrap; }

  .divider { position: absolute; left: 292px; top: 166px; width: 3px; height: 196px; background: var(--slate); }

  .contact { position: absolute; left: 316px; top: 178px; list-style: none; }
  .contact__row { display: flex; align-items: center; height: 26px; margin-bottom: 26px; }
  .contact__label {
    flex: none; width: 102px; height: 26px; border-radius: 6px;
    background: var(--label-bg); color: #fff;
    font-size: 17px; font-weight: 800; padding-left: 6px; line-height: 26px;
  }
  .contact__value { font-size: 19px; color: var(--ink); margin-left: 8px; white-space: nowrap; }
  .contact__value--email { font-size: 17px; letter-spacing: -0.2px; }

  .back-art { position: absolute; inset: 0; }

  .brand--back {
    left: 20px; top: 150px; width: 270px; height: 120px; gap: 12px;
  }
  .brand--back .brand__mark { width: 22px; height: 22px; }
  .brand--back .brand__name { font-size: 46px; }

  .services {
    position: absolute; left: 342px; top: 24px; width: 360px;
    list-style: none; text-align: center; color: #fff;
    font-weight: 700; font-size: 25px; line-height: 36px;
  }
  .services__item { margin-bottom: 36px; }
  .services__item:first-child { margin-bottom: 34px; }
  .services__web { position: absolute; left: 342px; top: 376px; width: 380px; text-align: center; color: #fff; font-weight: 800; font-size: 25px; letter-spacing: 0.4px; }
</style>
</head>
<body>
<main class="canvas">

  <section class="card card--front" aria-label="Business card front">
    <div class="warm-band warm-band--top-left"></div>
    <div class="warm-band warm-band--top-right"></div>
    <div class="brand">
      <span class="brand__mark"></span>
      <span class="brand__name">HomeWise</span>
    </div>

    <div class="person">
      <p class="person__name">Danielle Reyes Crawford</p>
      <p class="person__creds">OTR/L, CAPS, ECHM</p>
      <p class="person__role">Occupational Therapist,<br>Home Modification &amp;<br>Accessibility Specialist</p>
    </div>

    <div class="divider"></div>

    <ul class="contact">
      <li class="contact__row"><span class="contact__label">phone:</span><span class="contact__value">(503)218-4057</span></li>
      <li class="contact__row"><span class="contact__label">email:</span><span class="contact__value contact__value--email">homewiseforyears@nestmail.example</span></li>
      <li class="contact__row"><span class="contact__label">website:</span><span class="contact__value">www.homewiseforyears.com</span></li>
      <li class="contact__row"><span class="contact__label">CCB #:</span><span class="contact__value">487315</span></li>
    </ul>

    <div class="warm-band warm-band--bottom"></div>
  </section>

  <section class="card card--back" aria-label="Business card back">
    <svg class="back-art" width="745" height="424" viewBox="0 0 745 424" aria-hidden="true">
      <defs>
        <radialGradient id="warmGlow" cx="0.55" cy="0.5" r="0.75">
          <stop offset="0" stop-color="#ee7d1b"/>
          <stop offset="0.5" stop-color="#c2501a"/>
          <stop offset="1" stop-color="#8e2a12"/>
        </radialGradient>
      </defs>
      <rect width="745" height="424" fill="url(#warmGlow)"/>
      <circle cx="94" cy="212" r="258" fill="#ffffff"/>
    </svg>

    <div class="brand brand--back">
      <span class="brand__mark"></span>
      <span class="brand__name">HomeWise</span>
    </div>

    <ul class="services">
      <li class="services__item">Occupational Therapy</li>
      <li class="services__item">Home safety &amp;<br>accessibility<br>assessments</li>
      <li class="services__item">Home modification<br>consulting, project<br>management</li>
    </ul>
    <p class="services__web">www.homewiseforyears.com</p>
  </section>

</main>
</body>
</html>
```